Harbourline Blinds & Shutters

It Needs to look classy as my target is the upper end of the blind market
I need a Logo design on front and description on back of what i do:
- Roller Blinds
- Vertical Blinds
- Venetian Blinds
- Plantation Shutters
- Aluminum External Shutters
and contact details
Declan
0418275063
and
Trent
0419852306
Updates
Hi Guys,
Sorry for the no feedback but i was waiting on my logo design. But its done now i have uploaded it. so if you could take a look and send through some designs
Reason: my logo was just finished an i just uploaded it today really dont understand why my deadline has been rached foe my bizcards as it states no deadline. But please extend
Target Market(s)
People that live on the coast and are looking for classy good quality blinds and shutters
Font styles to use
Other font styles liked:
- Copperplate Gothic,open to suggestion
Look and feel
Each slider illustrates characteristics of the customer's brand and the style your logo design should communicate.

```html
<!DOCTYPE html>
<html lang="en">
<head>
<meta charset="utf-8">
<title>Harbourline Blinds &amp; Shutters — Business Cards</title>
<link rel="stylesheet" href="https://fonts.googleapis.com/css2?family=Cabin:ital,wght@0,600;0,700;1,600&family=Great+Vibes&display=swap">
<style>
  :root {
    --canvas: #ffffff;
    --card: #000000;
    --gold: #c99a0c;
    --gold-light: #e0b21e;
    --gold-dark: #9c7403;
    --white: #ffffff;
  }
  * { margin: 0; padding: 0; box-sizing: border-box; }
  html, body {
    width: 1200px; height: 1000px; overflow: hidden;
    background: var(--canvas);
  }
  .sheet { position: relative; width: 1200px; height: 1000px; }

  .card {
    position: absolute;
    width: 740px; height: 385px;
    background: var(--card);
    overflow: hidden;
    font-family: "Cabin", sans-serif;
    box-shadow: 0 14px 28px rgba(0,0,0,0.35);
  }
  .card__band {
    position: absolute; left: 0; right: 0; bottom: 0; height: 14px;
    background: linear-gradient(180deg, var(--gold-light), var(--gold-dark));
  }
  .card__accent {
    position: absolute;
    background: radial-gradient(ellipse at center, var(--gold-light), var(--gold-dark));
  }

  /* front */
  .card--front { left: 50px; top: 55px; }
  .card--front .card__accent {
    left: 0; top: 0; width: 260px; height: 75px;
    border-bottom-right-radius: 60px;
  }
  .brand {
    position: absolute; left: 65px; top: 156px;
    font-weight: 700; font-size: 32px; letter-spacing: 0.5px;
    color: var(--white); text-transform: uppercase;
    white-space: nowrap; line-height: 1;
  }

  /* back */
  .card--back { left: 390px; top: 505px; width: 715px; height: 385px; }
  .card--back .card__accent {
    right: 0; top: 0; width: 115px; height: 60px;
    border-bottom-left-radius: 40px;
  }
  .script {
    position: absolute; font-family: "Great Vibes", cursive;
    color: var(--white); line-height: 1;
  }
  .script--contact { left: 82px; top: 20px; font-size: 30px; }
  .script--for { left: 358px; top: 140px; font-size: 26px; }

  .contacts {
    position: absolute; left: 140px; top: 0; width: 210px; height: 220px;
    color: var(--gold); font-style: italic; font-weight: 600;
  }
  .contacts p {
    position: absolute; left: 0; right: 0; text-align: center; line-height: 1;
  }
  .contacts__name { font-size: 20px; }
  .contacts__phone { font-size: 22px; }
  .contacts__and { font-size: 13px; }
  .contacts__name--first { top: 47px; }
  .contacts__phone--first { top: 84px; }
  .contacts__and { top: 114px; }
  .contacts__name--second { top: 144px; }
  .contacts__phone--second { top: 184px; }

  .services {
    position: absolute; left: 418px; top: 0;
    list-style: none; color: var(--gold);
    font-weight: 600; font-size: 19px; line-height: 1;
  }
  .services li { position: absolute; left: 0; white-space: nowrap; }
  .services li:nth-child(1) { top: 166px; }
  .services li:nth-child(2) { top: 202px; }
  .services li:nth-child(3) { top: 238px; }
  .services li:nth-child(4) { top: 276px; }
  .services li:nth-child(5) { top: 314px; }
</style>
</head>
<body>
<main class="sheet">

  <section class="card card--front" aria-label="Business card front">
    <div class="card__accent" role="img" aria-label="Gold decorative corner accent"></div>
    <h1 class="brand">Harbourline Blinds &amp; Shutters</h1>
    <div class="card__band"></div>
  </section>

  <section class="card card--back" aria-label="Business card back">
    <div class="card__accent" role="img" aria-label="Gold decorative corner accent"></div>
    <span class="script script--contact">Contact</span>
    <div class="contacts">
      <p class="contacts__name contacts__name--first">Declan</p>
      <p class="contacts__phone contacts__phone--first">0418275063</p>
      <p class="contacts__and">&amp;</p>
      <p class="contacts__name contacts__name--second">Trent</p>
      <p class="contacts__phone contacts__phone--second">0419852306</p>
    </div>
    <span class="script script--for">for</span>
    <ul class="services">
      <li>- Roller Blinds</li>
      <li>- Vertical Blinds</li>
      <li>- Venetian Blinds</li>
      <li>- Plantation Shutters</li>
      <li>- Aluminum External Shutters</li>
    </ul>
    <div class="card__band"></div>
  </section>

</main>
</body>
</html>
```